Keep Harbor Homes. Avoid short sale, foreclosure, repossession, negative credit inquires and all other negative actions associated with your real estate.

Call 844-27-LUMEN or info@keepharborhomes.example

```html
<!DOCTYPE html>
<html lang="en">
<head>
<meta charset="utf-8">
<title>Keep Harbor Homes – Postcard</title>
<link href="https://fonts.googleapis.com/css2?family=Arimo:wght@700&family=Lato:wght@400;700&display=swap" rel="stylesheet">
<style>
  :root {
    --backdrop: #7a7a7a;
    --cocoa: #2b1913;
    --cocoa-deep: #1f120d;
    --sepia-light: #b89a7a;
    --sepia-mid: #7c5c43;
    --yellow: #f2e829;
    --ink: #111111;
    --white: #ffffff;
    --skin: #c9a58a;
    --denim: #6f86a3;
  }
  * { box-sizing: border-box; margin: 0; padding: 0; }
  html, body {
    width: 1200px; height: 1200px; overflow: hidden;
    background: var(--backdrop);
  }
  .postcard {
    position: absolute; left: 0; top: 192px;
    width: 1200px; height: 816px;
    background: var(--cocoa);
    overflow: hidden;
  }
  .house-photo {
    position: absolute; left: 0; top: 0; width: 760px; height: 470px;
    background:
      radial-gradient(ellipse at 60% 40%, var(--sepia-light) 0%, var(--sepia-mid) 45%, rgba(43,25,19,0) 80%),
      linear-gradient(180deg, #8a6a50 0%, var(--cocoa) 100%);
  }
  .call-band {
    position: absolute; left: 0; top: 636px; width: 1200px; height: 95px;
    background: var(--yellow);
  }
  .contact-band {
    position: absolute; left: 0; top: 731px; width: 1200px; height: 85px;
    background: var(--white);
  }
  .child-photo {
    position: absolute; left: 720px; top: 0; width: 400px; height: 816px;
    background: linear-gradient(180deg, #8b6a55 0%, var(--skin) 30%, #d8c4ae 60%, var(--denim) 78%, #b49a80 100%);
  }
  .headline {
    position: absolute; left: 46px; top: 268px;
    font-family: "Arimo", Arial, sans-serif; font-weight: 700;
    font-size: 88px; line-height: 92px; color: var(--white);
  }
  .benefits {
    position: absolute; left: 50px; top: 462px; width: 600px;
    list-style: none;
    display: grid; grid-template-columns: 262px 300px; row-gap: 4px;
    font-family: "Lato", sans-serif; font-size: 24px; line-height: 30px; color: var(--white);
  }
  .benefits li { padding-left: 26px; position: relative; }
  .benefits li::before {
    content: ""; position: absolute; left: 2px; top: 8px;
    width: 15px; height: 15px; border-radius: 50%; background: var(--yellow);
  }
  .benefits-note {
    position: absolute; left: 68px; top: 543px; width: 560px;
    font-family: "Lato", sans-serif; font-size: 24px; line-height: 32px; color: var(--white);
  }
  .call-line {
    position: absolute; left: 48px; top: 648px;
    font-family: "Lato", sans-serif; font-weight: 700;
    font-size: 62px; line-height: 72px; color: var(--ink);
  }
  .email-line {
    position: absolute; left: 56px; top: 745px;
    display: flex; align-items: center; gap: 18px;
    font-family: "Lato", sans-serif; font-size: 30px; line-height: 40px; color: var(--ink);
  }
</style>
</head>
<body>
  <main class="postcard">
    <div class="house-photo" role="img" aria-label="Sepia photo of a large two-storey family house under a cloudy sky"></div>
    <div class="call-band"></div>
    <div class="contact-band"></div>
    <div class="child-photo" role="img" aria-label="Photo of a sad young girl hugging a teddy bear while sitting on a suitcase"></div>

    <h1 class="headline">Keep Harbor<br>Homes.</h1>

    <ul class="benefits">
      <li>Avoid short sale</li>
      <li>foreclosure,</li>
      <li>repossession</li>
      <li>negative credit inquires</li>
    </ul>
    <p class="benefits-note">and all other negative actions associated with your real estate.</p>

    <p class="call-line">Call 844-27-LUMEN</p>
    <p class="email-line">
      <svg width="32" height="20" viewBox="0 0 32 20" aria-hidden="true">
        <rect x="1" y="1" width="30" height="18" fill="none" stroke="#111" stroke-width="2"/>
        <path d="M1 1 L16 12 L31 1 M1 19 L12 9 M31 19 L20 9" fill="none" stroke="#111" stroke-width="2"/>
      </svg>
      info@keepharborhomes.example
    </p>
  </main>
</body>
</html>
```